Wattlegrove Campus Lodgings needs a business card design

Hi Guys,

We are a Student Accommodation company in Australia. We already have a logo which I will submit.

I will require the design of the business cards from you.

I am after something that looks clean, modern and that people feel interested and actually want to contact us.

We would like to see designs that are innovative.

On the business cards I will require to have:

Employee Name
Position
Phone number
Email
Facebook page

I hope you can help me with this project guys as I have heard really good things from you.

```html
<!DOCTYPE html>
<html lang="en">
<head>
<meta charset="utf-8">
<title>Wattlegrove Campus Lodgings – Business Card</title>
<link href="https://fonts.googleapis.com/css2?family=Oswald:wght@400;600&family=Open+Sans:wght@400;600&display=swap" rel="stylesheet">
<style>
  :root{
    --bg:#e9e6e1;
    --card:#ffffff;
    --paper:#f4f4f4;
    --gold:#f0aa00;
    --green:#129b1e;
    --green-dark:#0b6f14;
    --green-pale:#a8e29a;
    --ink:#3b3b3b;
    --rule:#c9c9c9;
  }
  *{box-sizing:border-box;margin:0;padding:0}
  html,body{width:1069px;height:1200px;overflow:hidden;background:var(--bg)}
  body{position:relative;font-family:"Open Sans",Arial,sans-serif}

  .card{
    position:absolute;left:94px;width:880px;height:503px;
    background:var(--card);border:16px solid var(--gold);
    box-shadow:0 6px 18px rgba(0,0,0,.18);overflow:hidden;
  }
  .card--front{top:48px}
  .card--back{top:640px}

  /* brand name lockup */
  .brand{display:flex;align-items:center;gap:16px}
  .brand__mark{width:26px;height:26px;background:var(--gold);flex:none}
  .brand__name{
    font-family:"Oswald",Arial,sans-serif;font-weight:600;color:var(--green);
    text-transform:uppercase;line-height:1.05;letter-spacing:.5px
  }

  /* front */
  .card--front .inner{position:absolute;inset:0;background:var(--paper)}
  .card--front .brand{position:absolute;left:170px;top:165px}
  .card--front .brand__name{font-size:40px}
  .front-band{
    position:absolute;top:0;right:0;width:74px;height:100%;background:var(--green);
    display:flex;align-items:center;justify-content:center
  }
  .front-band__web{
    transform:rotate(90deg);white-space:nowrap;color:var(--green-pale);
    font-size:13px;letter-spacing:1px
  }

  /* back */
  .card--back .inner{position:absolute;inset:0;background:var(--paper)}
  .card--back .brand{position:absolute;left:34px;top:60px}
  .card--back .brand__name{font-size:30px}
  .contacts{
    position:absolute;right:0;top:0;height:260px;display:flex
  }
  .contacts__list{
    list-style:none;padding:44px 26px 0 0;text-align:right;
    font-size:15px;color:var(--ink);line-height:34px
  }
  .contacts__icons{
    width:56px;border-left:2px solid var(--rule);border-bottom:3px solid var(--gold);
    height:180px;display:flex;flex-direction:column;align-items:center;padding-top:52px;gap:14px
  }
  .contacts__icons svg{width:18px;height:18px;fill:none;stroke:var(--ink);stroke-width:1.8}
  .back-band{
    position:absolute;left:0;right:0;top:272px;height:130px;background:var(--green);
    display:flex;align-items:center;justify-content:space-between;padding:0 40px 0 50px
  }
  .person__name{
    font-family:"Oswald",Arial,sans-serif;font-weight:600;font-size:62px;
    color:var(--green-dark);text-transform:uppercase;letter-spacing:2px
  }
  .person__role{
    color:var(--green-pale);font-size:15px;letter-spacing:2px;text-transform:uppercase;align-self:flex-start;margin-top:18px
  }
  .address{
    position:absolute;left:0;right:0;bottom:0;height:69px;display:flex;align-items:center;
    padding-left:280px;font-size:17px;color:var(--ink)
  }
</style>
</head>
<body>

<section class="card card--front" aria-label="Card front">
  <div class="inner">
    <div class="brand">
      <span class="brand__mark"></span>
      <span class="brand__name">Wattlegrove<br>Campus Lodgings</span>
    </div>
    <div class="front-band"><span class="front-band__web">www.wattlegrove.com.au</span></div>
  </div>
</section>

<section class="card card--back" aria-label="Card back">
  <div class="inner">
    <div class="brand">
      <span class="brand__mark"></span>
      <span class="brand__name">Wattlegrove<br>Campus Lodgings</span>
    </div>

    <div class="contacts">
      <ul class="contacts__list">
        <li>02 5550 1482</li>
        <li>0400 555 736</li>
        <li>hello@wattlegrove.com.au</li>
        <li>www.wattlegrove.com.au</li>
      </ul>
      <div class="contacts__icons">
        <svg viewBox="0 0 24 24" aria-label="Phone"><path d="M5 3h4l2 5-3 2a12 12 0 0 0 6 6l2-3 5 2v4a2 2 0 0 1-2 2A18 18 0 0 1 3 5a2 2 0 0 1 2-2z"/></svg>
        <svg viewBox="0 0 24 24" aria-label="Mobile"><rect x="7" y="2" width="10" height="20" rx="2"/><path d="M11 18h2"/></svg>
        <svg viewBox="0 0 24 24" aria-label="Email"><rect x="3" y="5" width="18" height="14"/><path d="M3 5l9 8 9-8"/></svg>
        <svg viewBox="0 0 24 24" aria-label="Web"><circle cx="12" cy="12" r="9"/><path d="M3 12h18M12 3c3 3 3 15 0 18M12 3c-3 3-3 15 0 18"/></svg>
      </div>
    </div>

    <div class="back-band">
      <span class="person__name">Aidan Marlow</span>
      <span class="person__role">General Manager</span>
    </div>

    <p class="address">27 Banksia Lane, Level 3, Carlton VIC</p>
  </div>
</section>

</body>
</html>
```